Visitenkarten-Design für Catering/ Liefertouren
Vielen Dank für die professionelle Zusammenarbeit. Änderungen wurden schnell und treffend umgesetzt. Wir sind mit dem Ergebnis sehr zufrieden.
Zielgruppe
Catering/ Liefertouren für hochwertige selbstgemachte Quiches/ französische Tartes, Suppen, Currys
Aufgabenstellung
2 Visitenkarten im Format DIN6 (21x10,5) lang die sich auf der 1. (Bild) Seite unterscheiden aber mit identischer 2. Seite.
Karte 'Quiche' 1. Seite:
'Quiche '
L'art de la tarte - depuis 2011
Quiches, Soups, Currys,
Catering, Abholung, Liefertouren
www.Kovendo.de,
info@kovendo.de
Karte 'Soups' 1. Seite:
'KovendoChicken, KovendoTofu'
2. Seite (für beide Karten identisch)
Seite soll eine Art Vorlage sein und besteht lediglich aus einer gestalterischen 'Umrahmung' und unserem Logo am unteren Seitenrand. Der Durchmesser des Logos soll max. 15% der gesamten Seitenlänge betragen.
Seite wird von uns mit Angeboten/ Aktionen bedruckt in kleiner Stückzahl nachträglich bedruckt.
1. Seiten (Quer- oder Hochformat je nach Bild möglich).
2. Seite im Hochformat.
Keine Vorgaben bzgl. Schrifttyp.

```html
<!DOCTYPE html>
<html lang="de">
<head>
<meta charset="utf-8">
<title>Kovendo – Visitenkarten</title>
<link rel="stylesheet" href="https://fonts.googleapis.com/css2?family=Sorts+Mill+Goudy&display=swap">
<style>
  :root {
    --paper: #ffffff;
    --navy: #050d1d;
    --ink: #ffffff;
    --accent-red: #b3121b;
    --logo-brown: #3d2219;
    --card-w: 361px;
    --card-h: 506px;
  }
  * { margin: 0; padding: 0; box-sizing: border-box; }
  html, body {
    width: 1200px; height: 589px; overflow: hidden;
    background: var(--paper);
    font-family: "Sorts Mill Goudy", Georgia, serif;
    color: var(--ink);
  }
  .card {
    position: absolute; top: 38px;
    width: var(--card-w); height: var(--card-h);
    background: var(--navy);
    overflow: hidden;
  }
  .card--quiche { left: 36px; }
  .card--soups { left: 426px; }
  .card--back { left: 815px; }

  .card__visual {
    position: absolute; left: 0; top: 0;
    width: var(--card-w); height: var(--card-h);
  }
  .card__title {
    position: absolute; top: 18px; left: 0; right: 0;
    text-align: center; font-size: 44px; line-height: 48px;
    font-weight: 400; letter-spacing: 1px;
  }
  .card__tagline {
    position: absolute; top: 84px; left: 0; right: 0;
    text-align: center; font-size: 11px; line-height: 14px; letter-spacing: 0.3px;
  }
  .card__rule {
    position: absolute; top: 103px; left: 50%;
    width: 130px; height: 1px; margin-left: -65px;
    background: var(--accent-red);
  }
  .card__services {
    position: absolute; top: 108px; left: 0; right: 0;
    text-align: center; font-size: 10.5px; line-height: 14px; letter-spacing: 0.2px;
  }
  .card__contact {
    position: absolute; top: 464px; left: 0; right: 0; height: 28px;
    display: flex; justify-content: center; align-items: center;
    font-size: 11px; letter-spacing: 0.3px;
  }
  .card__contact span { padding: 0 11px; white-space: nowrap; }
  .card__contact .divider {
    width: 1px; height: 27px; padding: 0;
    background: var(--accent-red);
  }

  .back__ornament {
    position: absolute; left: 0; top: 405px;
    width: var(--card-w); height: 40px;
    background: linear-gradient(90deg, rgba(255,255,255,0.04), rgba(255,255,255,0.12), rgba(255,255,255,0.04));
    border-radius: 20px;
  }
  .back__logo {
    position: absolute; left: 130px; top: 362px;
    width: 106px; height: 106px; border-radius: 50%;
    background: var(--logo-brown);
    border: 2px solid var(--ink);
    display: flex; align-items: center; justify-content: center;
    font-size: 21px;
  }
</style>
</head>
<body>

<section class="card card--quiche">
  <svg class="card__visual" viewBox="0 0 361 506" role="img" aria-label="Foto: Gemüse-Quiche mit Tomaten und Zucchini auf dunkler Schieferplatte">
    <defs>
      <linearGradient id="quicheTones" x1="0" y1="0" x2="0.6" y2="1">
        <stop offset="0" stop-color="#2c3a55"/>
        <stop offset="0.4" stop-color="#4a4a52"/>
        <stop offset="0.7" stop-color="#c7773a"/>
        <stop offset="1" stop-color="#b5602c"/>
      </linearGradient>
    </defs>
    <path d="M0,150 C150,145 260,165 320,200 C340,212 355,222 361,228 L361,442 L120,442 C70,430 25,400 0,372 Z" fill="url(#quicheTones)"/>
  </svg>
  <h1 class="card__title">Quiche</h1>
  <p class="card__tagline">L'art de la tarte - depuis 2011</p>
  <div class="card__rule"></div>
  <p class="card__services">Tartes, Suppen, Currys, Catering, Abholung, Lieferservice</p>
  <div class="card__contact">
    <span>www.kovendo.de</span><span class="divider"></span>
    <span>+49 (0) 89-4172 5083</span><span class="divider"></span>
    <span>info@kovendo.de</span>
  </div>
</section>

<section class="card card--soups">
  <svg class="card__visual" viewBox="0 0 361 506" role="img" aria-label="Foto: Tomatensuppe mit Croûtons im Gusseisentopf, umgeben von Paprika, Kräutern und Gewürzen">
    <defs>
      <radialGradient id="soupTones" cx="0.5" cy="0.55" r="0.6">
        <stop offset="0" stop-color="#b8462a"/>
        <stop offset="0.35" stop-color="#4a4a4c"/>
        <stop offset="0.7" stop-color="#2f4a25"/>
        <stop offset="1" stop-color="#1a2418"/>
      </radialGradient>
    </defs>
    <path d="M0,150 L270,150 C320,165 355,200 361,222 L361,445 L55,445 C30,425 8,400 0,376 Z" fill="url(#soupTones)"/>
  </svg>
  <h1 class="card__title">Soups</h1>
  <p class="card__tagline">L'art de la tarte - depuis 2011</p>
  <div class="card__rule"></div>
  <p class="card__services">Tartes, Suppen, Currys, Catering, Abholung, Lieferservice</p>
  <div class="card__contact">
    <span>www.kovendo.de</span><span class="divider"></span>
    <span>+49 (0) 89-4172 5083</span><span class="divider"></span>
    <span>info@kovendo.de</span>
  </div>
</section>

<section class="card card--back">
  <div class="back__ornament" role="img" aria-label="Geschwungene weiße Zierlinie über die Kartenbreite"></div>
  <div class="back__logo">Kovendo</div>
</section>

</body>
</html>
```